Harborline Motors LLC

Car Dealer Customer Service
Address: 2741 Linden Avenue, Shelbyville, TN 37162
web: www.harborlinemotorstn.net
email: harborlinemotorstn@mailbox-example.net
Phone: (931) 555-0148
Phone: (629) 555-0173

```html
<!DOCTYPE html>
<html lang="en">
<head>
<meta charset="utf-8">
<title>Harborline Motors LLC – Business Card</title>
<link href="https://fonts.googleapis.com/css2?family=Montserrat:wght@800&family=Source+Sans+3:wght@400&display=swap" rel="stylesheet">
<style>
  :root {
    --brand-blue: #1b73a8;
    --brand-gold: #eab03f;
    --tag-gold: #e8a42c;
    --card-white: #ffffff;
    --page-bg: #f3f3f3;
  }
  * { margin: 0; padding: 0; box-sizing: border-box; }
  html, body { width: 1200px; height: 900px; overflow: hidden; background: var(--page-bg); }
  .sheet { position: relative; width: 1200px; height: 900px; }
  .card {
    position: absolute; left: 285px; width: 630px; height: 360px;
    background: var(--card-white);
  }
  .card--front { top: 63px; }
  .card--back { top: 478px; }

  .front-name {
    position: absolute; left: 0; right: 0; top: 160px;
    display: flex; align-items: center; justify-content: center; gap: 12px;
    font-family: "Montserrat", sans-serif; font-weight: 800;
    font-size: 29px; letter-spacing: 0.5px; color: var(--brand-blue);
  }
  .front-name .dot { width: 16px; height: 16px; border-radius: 50%; background: var(--brand-gold); }

  .back-brand {
    position: absolute; right: 25px; top: 120px; text-align: right;
  }
  .back-brand .name {
    font-family: "Montserrat", sans-serif; font-weight: 800;
    font-size: 22px; line-height: 1; color: var(--brand-blue); letter-spacing: 0.3px;
  }
  .back-brand .tagline {
    margin-top: 6px;
    font-family: "Source Sans 3", sans-serif; font-size: 13.5px;
    color: var(--tag-gold); text-transform: uppercase; letter-spacing: 0.2px;
  }
  .divider {
    position: absolute; left: 26px; width: 579px; top: 202px;
    height: 2px; background: var(--brand-gold);
  }
  .contact {
    position: absolute; font-family: "Source Sans 3", sans-serif;
    font-size: 16.5px; line-height: 1.3; color: var(--brand-blue);
  }
  .contact-row { position: absolute; left: 29px; display: flex; align-items: center; gap: 18px; }
  .contact-row.phone { top: 222px; }
  .contact-row.mail { top: 261px; }
  .contact-row.web { top: 295px; }
  .icon {
    width: 27px; height: 27px; border-radius: 5px; background: var(--brand-blue);
    display: flex; align-items: center; justify-content: center; flex: none;
  }
  .icon svg { width: 17px; height: 17px; }
  .contact-row.address { left: 386px; top: 220px; align-items: flex-start; }
</style>
</head>
<body>
<div class="sheet">
  <section class="card card--front">
    <div class="front-name"><span class="dot"></span>HARBORLINE MOTORS</div>
  </section>

  <section class="card card--back">
    <div class="back-brand">
      <div class="name">HARBORLINE MOTORS</div>
      <div class="tagline">Car Dealer Customer Service</div>
    </div>
    <div class="divider"></div>

    <div class="contact contact-row phone">
      <span class="icon"><svg viewBox="0 0 24 24" fill="none" stroke="#fff" stroke-width="2.2" stroke-linejoin="round"><path d="M5 3h4l2 5-2.5 1.5a11 11 0 0 0 6 6L16 13l5 2v4a2 2 0 0 1-2 2A17 17 0 0 1 3 5a2 2 0 0 1 2-2z"/></svg></span>
      <span>(931) 555-0148<br>(629) 555-0173</span>
    </div>
    <div class="contact contact-row mail">
      <span class="icon"><svg viewBox="0 0 24 24" fill="none" stroke="#fff" stroke-width="2"><rect x="3" y="5" width="18" height="14"/><path d="M3 5l9 8 9-8"/></svg></span>
      <span>harborlinemotorstn@mailbox-example.net</span>
    </div>
    <div class="contact contact-row web">
      <span class="icon"><svg viewBox="0 0 24 24" fill="none" stroke="#fff" stroke-width="2"><circle cx="12" cy="12" r="9"/><ellipse cx="12" cy="12" rx="4" ry="9"/><path d="M3 12h18"/></svg></span>
      <span>www.harborlinemotorstn.net</span>
    </div>
    <div class="contact contact-row address">
      <span class="icon" style="margin-top:6px"><svg viewBox="0 0 24 24" fill="#fff"><path d="M12 2a7 7 0 0 0-7 7c0 5 7 13 7 13s7-8 7-13a7 7 0 0 0-7-7zm0 10a3 3 0 1 1 0-6 3 3 0 0 1 0 6z"/></svg></span>
      <span>2741 Linden Avenue,<br>Shelbyville,<br>TN 37162</span>
    </div>
  </section>
</div>
</body>
</html>
```